Lumora vale- referral cards for new customers

Hey,

I would like 1 set of business cards with the following details:

10% off any sales / coupon code
Our phone number: 4702938165
Menu :Lumoravale.example (for the menu)
A line left blank to hand write an activation code: either on top or just on one side

Include the Lumora Vale logo ( your choice of black or white logo)
This card is to drive orders for people to order a cannabis order with Lumora Vale. Please make the logo a large part of the card on both sides.

Target Market(s)

People who consume cannabis 21 and up

Industry/Entity Type

Business

Contact Information for Business Card

This business card will be given to customers so they can then give it to other customers and generate referalls. We need this card to be elegant, impressionable, professional, and something worth keeping and passing to friends.

Font styles to use
Decorative
Script

Colors
33a6d7
85acd3
3176b5
0455a3
0592cd
85cae6
cee9f5
eaf1f7
757575

Requirements
Must have
• Our website
• Phone Number
• The 10% off an order
• Spot for activation code
Nice to have
• Eye catching design
• Look classy
• Textured feel or textured look
Should not have
• Do not look super cannabis heady
• Do not look attractive to children

```html
<!DOCTYPE html>
<html lang="en">
<head>
<meta charset="utf-8">
<title>Lumora Vale – Referral Cards</title>
<link href="https://fonts.googleapis.com/css2?family=Roboto+Condensed:wght@400&display=swap" rel="stylesheet">
<style>
  :root {
    --backdrop: #4a4641;
    --olive: #575a2a;
    --olive-ink: #4f5425;
    --card-white: #ffffff;
    --ink-dark: #1f1f1f;
    --ink-grey: #2b2b2b;
    --rule: #5d6230;
  }
  * { margin: 0; padding: 0; box-sizing: border-box; }
  html, body {
    width: 1200px; height: 930px; overflow: hidden;
    background: var(--backdrop);
    font-family: "Roboto Condensed", "Arial Narrow", sans-serif;
  }
  .canvas { position: relative; width: 1200px; height: 930px; }
  .card {
    position: absolute; width: 620px; height: 354px;
    box-shadow: 0 10px 24px rgba(0,0,0,.35);
  }
  .card-back { left: 70px; top: 70px; background: var(--olive); }
  .card-front { left: 510px; top: 500px; background: var(--card-white); }

  .brand {
    position: absolute; display: flex; align-items: center; gap: 16px;
    color: var(--ink-dark); letter-spacing: 1px; white-space: nowrap;
  }
  .brand-dot { border-radius: 50%; background: var(--ink-dark); flex: none; }
  .card-back .brand { left: 50%; top: 50%; transform: translate(-50%, -50%); font-size: 64px; }
  .card-back .brand-dot { width: 46px; height: 46px; }
  .card-front .brand { right: 40px; top: 48px; font-size: 40px; gap: 12px; }
  .card-front .brand-dot { width: 30px; height: 30px; }

  .offer { position: absolute; left: 48px; top: 46px; }
  .offer-value { font-size: 30px; color: var(--olive-ink); line-height: 1; }
  .offer-note { font-size: 15px; color: var(--ink-grey); margin-top: 4px; }
  .activation {
    position: absolute; left: 48px; top: 140px; width: 230px;
    display: flex; align-items: flex-end; gap: 8px;
    font-size: 14px; color: var(--ink-grey);
  }
  .activation-blank { flex: 1; border-bottom: 1px solid var(--ink-grey); height: 16px; }

  .rule {
    position: absolute; left: 48px; right: 40px; top: 200px;
    height: 1.5px; background: var(--rule);
  }
  .contact {
    position: absolute; right: 40px; top: 222px;
    list-style: none; font-size: 17px; color: var(--ink-grey);
  }
  .contact li { display: flex; align-items: center; gap: 10px; margin-bottom: 8px; }
  .contact svg { width: 14px; height: 14px; }
  .person { position: absolute; left: 58px; top: 236px; }
  .person-name { font-size: 30px; color: var(--olive-ink); letter-spacing: .5px; line-height: 1; }
  .person-role { font-size: 19px; color: var(--ink-grey); margin-top: 4px; }
</style>
</head>
<body>
<main class="canvas">
  <section class="card card-back" aria-label="Card back">
    <div class="brand"><span class="brand-dot"></span><span>Lumora Vale</span></div>
  </section>

  <section class="card card-front" aria-label="Card front">
    <div class="offer">
      <p class="offer-value">10% OFF</p>
      <p class="offer-note">any order with your code</p>
    </div>
    <div class="activation"><span>Activation code</span><span class="activation-blank"></span></div>
    <div class="brand"><span class="brand-dot"></span><span>Lumora Vale</span></div>
    <div class="rule"></div>
    <ul class="contact">
      <li>
        <svg viewBox="0 0 16 16" aria-hidden="true"><path d="M4 1.5l2.2 3-1.3 1.6c.9 2 2.5 3.6 4.5 4.5l1.6-1.3 3 2.2-1.2 2.5C7.6 13.7 2.3 8.4 1.5 3.2z" fill="#555"/></svg>
        <span>4702938165</span>
      </li>
      <li>
        <svg viewBox="0 0 16 16" aria-hidden="true"><circle cx="8" cy="8" r="6.5" fill="none" stroke="#555" stroke-width="1.3"/><path d="M1.5 8h13M8 1.5c-3 3.5-3 9.5 0 13M8 1.5c3 3.5 3 9.5 0 13" fill="none" stroke="#555" stroke-width="1.1"/></svg>
        <span>www.lumoravale.example</span>
      </li>
    </ul>
    <div class="person">
      <p class="person-name">DARIA HOLT</p>
      <p class="person-role">Director</p>
    </div>
  </section>
</main>
</body>
</html>
```